Visitenkarten-Design für Sonnen-/Fensterschutz
Zielgruppe
KLR GmbH ist eine Firma, die Sonnenschutz und Fensterschutz anbieten.
'Ihr kompetenter Partner in Sachen Sonnenschutz- , Fenster- und Türtechnik. Sie erhalten echtes Handwerk aus dem Mühlviertel zu fairen Preisen.'
Unsere Zielgruppe sind Personen mit Haus, die am Land leben.
Firmenname: KLR GmbH
Slogan: Fenster & Sonnenschutz
Aufgabenstellung
Hier befindet sich das Logodesign: https://dl.qv/t-Rm8pQ2wZtB
Bitte ein schlichtes Design bereitstellen mit einer Dummy-Person:
Lutz Brenneke + Telefonnummer + Email
Die finalen Daten bitte erst am Schluss berücksichtigen (für Gewinnerdesign)
Gerne auch hintern + vorne bedruckbar bereitstellen.

```html
<!DOCTYPE html>
<html lang="de">
<head>
<meta charset="utf-8">
<title>KLR GmbH – Visitenkarte</title>
<link href="https://fonts.googleapis.com/css2?family=Poppins:wght@400;600;700&family=Source+Sans+3:wght@400;600&display=swap" rel="stylesheet">
<style>
  :root {
    --stage: #575757;
    --paper: #ffffff;
    --orange: #ef7d1f;
    --red: #e33d24;
    --text: #58585a;
    --muted: #8a8a8a;
    --divider: #f6d7bd;
  }
  * { margin: 0; padding: 0; box-sizing: border-box; }
  html, body { width: 1200px; height: 1200px; overflow: hidden; }
  body { background: var(--stage); position: relative; font-family: "Poppins", sans-serif; }

  .card { position: absolute; left: 247px; width: 669px; height: 433px; overflow: hidden; }
  .card--front { top: 112px; background: var(--paper); }
  .card--back { top: 616px; }

  .speed-lines { position: absolute; left: 0; top: 54px; }

  .brand { position: absolute; left: 372px; top: 46px; display: flex; align-items: center; gap: 14px; }
  .brand__mark { width: 54px; height: 54px; background: var(--orange); }
  .brand__name { font-family: "Poppins", sans-serif; font-weight: 700; font-size: 36px; line-height: 1; color: var(--orange); letter-spacing: 0.5px; }
  .brand__slogan { position: absolute; left: 440px; top: 100px; width: 199px; font-family: "Poppins", sans-serif; font-weight: 700; font-size: 11.5px; color: var(--red); letter-spacing: 0.2px; border-top: 2px solid var(--red); padding-top: 1px; }

  .company { position: absolute; left: 61px; top: 174px; font-size: 15px; color: var(--muted); font-weight: 600; }

  .contact { position: absolute; left: 61px; list-style: none; display: flex; align-items: flex-start; gap: 8px; font-size: 19px; line-height: 20px; color: var(--text); }
  .contact svg { flex: none; margin-top: 2px; }
  .contact--address { top: 211px; }
  .contact--phone { top: 264px; }
  .contact--mail { top: 298px; }

  .divider { position: absolute; left: 354px; top: 184px; width: 1px; height: 140px; background: var(--divider); }

  .person { position: absolute; left: 360px; width: 276px; top: 230px; text-align: center; font-family: "Source Sans 3", sans-serif; color: var(--text); }
  .person__name { font-size: 25px; font-weight: 400; line-height: 30px; }
  .person__role { font-size: 18px; font-weight: 600; line-height: 26px; }

  .base-band { position: absolute; left: 0; top: 400px; width: 100%; height: 12px; background: linear-gradient(90deg, var(--orange), var(--red) 55%, var(--red)); }

  .back-field { position: absolute; inset: 0; background: linear-gradient(180deg, var(--orange) 0%, #e8572a 35%, var(--red) 60%, var(--red) 100%); }
  .back-brand { position: absolute; inset: 0; display: flex; align-items: center; justify-content: center; }
  .back-brand__name { font-family: "Poppins", sans-serif; font-weight: 700; font-size: 72px; color: var(--paper); letter-spacing: 1px; }
</style>
</head>
<body>

<section class="card card--front" aria-label="Vorderseite">
  <svg class="speed-lines" width="372" height="70" viewBox="0 0 372 70" aria-hidden="true">
    <defs>
      <linearGradient id="lineGrad" x1="0" x2="1">
        <stop offset="0" stop-color="#ef7d1f"/>
        <stop offset="1" stop-color="#e33d24"/>
      </linearGradient>
    </defs>
    <rect x="0" y="4" width="355" height="3" fill="url(#lineGrad)"/>
    <rect x="0" y="14" width="360" height="4" fill="url(#lineGrad)"/>
    <rect x="0" y="25" width="366" height="3" fill="url(#lineGrad)"/>
    <rect x="0" y="34" width="372" height="11" fill="url(#lineGrad)"/>
  </svg>

  <div class="brand">
    <span class="brand__mark" aria-hidden="true"></span>
    <span class="brand__name">KLR GmbH</span>
  </div>
  <p class="brand__slogan">FENSTER &amp; SONNENSCHUTZ</p>

  <p class="company">KLR GmbH</p>

  <ul>
    <li class="contact contact--address">
      <svg width="22" height="22" viewBox="0 0 22 22" aria-hidden="true"><path d="M1 2 L21 11 L1 20 L6 11 Z" fill="none" stroke="#e33d24" stroke-width="2.2" stroke-linejoin="round"/></svg>
      <span>Lindenweg 7<br>30159 Hannover</span>
    </li>
    <li class="contact contact--phone">
      <svg width="20" height="20" viewBox="0 0 20 20" aria-hidden="true"><path d="M4 1 L8 5 L6 8 C7 11 9 13 12 14 L15 12 L19 16 L16 19 C8 19 1 12 1 4 Z" fill="#e33d24"/></svg>
      <span>+49 151 204 8836</span>
    </li>
    <li class="contact contact--mail">
      <svg width="20" height="18" viewBox="0 0 20 18" aria-hidden="true"><rect x="1" y="3" width="18" height="13" rx="1" fill="#e33d24"/><path d="M1 4 L10 11 L19 4" fill="none" stroke="#fff" stroke-width="1.6"/></svg>
      <span>+49 151 204 8836</span>
    </li>
  </ul>

  <div class="divider" aria-hidden="true"></div>

  <div class="person">
    <p class="person__name">Lutz Brenneke</p>
    <p class="person__role">Geschäftsführer</p>
  </div>

  <div class="base-band" aria-hidden="true"></div>
</section>

<section class="card card--back" aria-label="Rückseite">
  <div class="back-field" role="img" aria-label="Flächiges Muster aus Firmenzeichen in Orange und Rot"></div>
  <div class="back-brand">
    <span class="back-brand__name">KLR GmbH</span>
  </div>
</section>

</body>
</html>
```